GLOR Duet Summit Poster

We are a cellular therapy (bone marrow transplants, etc) accreditation foundation who needs a poster design for a small workshop that we are going to host within a large workshop. The workshop will 1) Educate doctors who inspect program trying to get accredited. 2) Educate programs on how to become accredited.

It will be printed and mounted on foam board for display at the GLOR booth in exhibition halls. Dimensions should be 11 x 17 inches.

Our website is www.glorsite-example.org. The design does not have to have the same theme/colors as our website.

The poster should have written:

Cellular Therapy Inspection and Accreditation Workshop
February 10th, 2015
QRV Duet Summit
San Diego, CA

The statement below should be in small, subtle text to allow room for the other information. All returns, italics, and trademark symbols must be used exactly as included below:

The Halbrook Institute of Health Sciences, Office for Ongoing Learning is accredited by the Certification Board for Ongoing Clinical Learning to provide continuing medical education for physicians.

The Halbrook Institute of Health Sciences, Office for Ongoing Learning designates this live activity for a maximum of 7.5 OLB KTV Tier 1 Point(s)™. Physicians should claim only credit commensurate with the extent of their participation in the activity.

It should also have our logo on it (I have attached 2, use the one that has the best resolution)

Let me know if there are any questions!

```html
<!DOCTYPE html>
<html lang="en">
<head>
<meta charset="utf-8">
<title>GLOR Duet Summit Poster</title>
<link rel="stylesheet" href="https://fonts.googleapis.com/css2?family=Arimo:ital,wght@0,400;0,700;1,400&display=swap">
<style>
  :root {
    --navy: #1d2c47;
    --sky-pale: #d9ebf6;
    --sky: #2fa3dd;
    --title-blue: #1f5f93;
    --white: #ffffff;
    --brand-red: #c8202f;
    --pattern-dark: #2a3a33;
    --pattern-olive: #8a9a5b;
    --pattern-teal: #4f8f8c;
    --photo-dusk: #3a5a86;
    --photo-glow: #c9a36a;
  }
  * { margin: 0; padding: 0; box-sizing: border-box; }
  html, body { width: 778px; height: 1200px; overflow: hidden; background: var(--white); }
  body { font-family: "Arimo", Arial, sans-serif; }
  .poster { position: relative; width: 778px; height: 1200px; background: var(--white); overflow: hidden; }

  .date-band {
    position: absolute; left: 0; top: 0; width: 778px; height: 112px;
    background: var(--navy); color: var(--white);
    font-size: 25px; font-weight: 700; letter-spacing: 0.5px;
    padding: 30px 0 0 30px;
  }
  .side-pattern {
    position: absolute; left: 0; top: 112px; width: 222px; height: 1088px;
    background: linear-gradient(160deg, var(--pattern-olive) 0%, var(--pattern-dark) 35%, var(--pattern-teal) 60%, var(--pattern-dark) 80%, var(--pattern-olive) 100%);
  }
  .title-panel {
    position: absolute; left: 228px; top: 122px; width: 550px; height: 132px;
    background: var(--sky-pale); color: var(--title-blue);
    padding: 30px 0 0 34px;
    font-size: 27px; line-height: 1.28; font-weight: 400;
  }
  .venue-photo {
    position: absolute; left: 228px; top: 254px; width: 550px; height: 322px;
    background: linear-gradient(180deg, var(--photo-dusk) 0%, #5d7da6 55%, var(--photo-glow) 78%, #4a4a52 100%);
  }
  .event-panel {
    position: absolute; left: 228px; top: 576px; width: 550px; height: 440px;
    background: var(--sky); color: var(--white);
  }
  .event-name {
    position: absolute; left: 34px; top: 86px;
    font-size: 38px; line-height: 1.2; font-weight: 400;
  }
  .accreditation-note {
    position: absolute; left: 228px; top: 284px; width: 292px;
    font-size: 10.5px; line-height: 1.32;
  }
  .accreditation-note p + p { margin-top: 4px; }
  .brand {
    position: absolute; right: 26px; bottom: 34px;
    display: flex; align-items: center; gap: 10px;
    color: var(--brand-red); font-size: 46px; font-weight: 400;
  }
  .brand-dot { width: 16px; height: 16px; border-radius: 50%; background: var(--brand-red); }
</style>
</head>
<body>
<main class="poster">
  <header class="date-band">FEBRUARY 10th, 2015</header>

  <div class="side-pattern" role="img" aria-label="Decorative column of rounded squares in olive, teal and dark green tones"></div>

  <h1 class="title-panel">Cellular Therapy Inspection<br>and Accreditation Workshop</h1>

  <div class="venue-photo" role="img" aria-label="Photograph of a modern glass conference building at dusk"></div>

  <section class="event-panel">
    <h2 class="event-name">QRV Duet Summit<br>San Diego, CA</h2>
    <div class="accreditation-note">
      <p>The Halbrook Institute of Health Sciences, Office for Ongoing Learning is accredited by the Certification Board for Ongoing Clinical Learning to provide continuing medical education for physicians.</p>
      <p>The Halbrook Institute of Health Sciences, Office for Ongoing Learning designates this live activity for a maximum of 7.5 <em>OLB KTV Tier 1 Point(s)™</em>. Physicians should claim only credit commensurate with the extent of their participation in the activity.</p>
    </div>
  </section>

  <div class="brand"><span class="brand-dot"></span>GLOR</div>
</main>
</body>
</html>
```